Scented Candle Company Sticker Design for Packaging

We need a Sticker design for our various scented candle packages. Our handmade candles incorperate hand crafted Chiyogami Paper imported from Japan, which is wrapped around the jar. Each of the scents have different papers assigned to them and although we would like a general design in which the text can be changed according to each scent we would also like if the beautiful Japanese paper designs could be subtly incorporated in the design.

We want the the text of the sticker and logo of our company to be printed in gold foil once printed and our featured logo image is of a Dogwood tree. We think that perhaps the inclusion of dogwood blossom/s might look nice in the design but is not a must have!

We are fond of the delicate and classic print designs and etching designs. We would also like the design to be in a portrait rectangle that is closer in the shape of a square/ or not too long of a rectangle, and, would like to have a boarder on the edge of the sticker (this could incorporate the blossom if you wish, I have attached an image for reference/ inspiration) but we are after something much more simplistic and draws less attention to the eye and connected in the boarder.

Our brand is elegant and classic and we would like to be in keeping with our style. We have attached some images of the candles and our logo for inspiration, we do not want the stickers for the candle themselves but rather to place on the packaging.

Ive left some information for one of the candle scents for this design but once again I would like to reiterate that the design should allow for interchangeable titles for the other fragrances.

Japanese Cherry Blossom(in smaller writing).
Japanese cherry blossom, Orange blossom, cinnamon.

Our candles are hand made in Australia and a made from 100% soy wax and we would like to to be presented on the label.

I would like to mention again that we are looking for an elegant and classic design. We are looking for a simplistic design/layout that also focuses on the fine details. It should be striking but also not overbearing with an air of sophistication with minimal to no use of colours in encouraged.

I have also attached a font that is matched to the "candle co." underneath the tree in the logo.
Updates

I only just posted the design request, but first created the brief on the 2nd. I would like more time for the designers to both see my review and have an adequate amount of time to work on the project.

Target Market(s)

Up Market Shoppers.

Font styles to use
Script
Other font styles liked:
• Acorn

Colors
fbfbfb

Requirements
Must have
• Logo on the sticker.
Nice to have
• Nice to have a dogwood blossom incorporated into the boarder but must be simplistic as it doesn't want to be the main focus of the sticker
Should not have
• Photographs in the sticker design. Must be graphic design. No to little colour.

```html
<!DOCTYPE html>
<html lang="en">
<head>
<meta charset="utf-8">
<title>Ashbrook Candle Co. – Packaging Sticker</title>
<link href="https://fonts.googleapis.com/css2?family=Cormorant+Garamond:wght@600&family=Great+Vibes&family=Alegreya+Sans:wght@400&display=swap" rel="stylesheet">
<style>
  :root {
    --gold: #c99a27;
    --paper: #ffffff;
    --trim: #8a8a8a;
    --page: #ffffff;
  }
  * { margin: 0; padding: 0; box-sizing: border-box; }
  html, body {
    width: 1200px;
    height: 723px;
    overflow: hidden;
    background: var(--page);
  }
  .canvas {
    position: relative;
    width: 1200px;
    height: 723px;
  }
  .sticker {
    position: absolute;
    left: 349px;
    top: 62px;
    width: 517px;
    height: 579px;
    background: var(--paper);
    border: 1px solid var(--trim);
  }
  .frame {
    position: absolute;
    left: 29px;
    top: 26px;
    width: 460px;
    height: 526px;
    border: 4px solid var(--gold);
    border-radius: 2px;
  }
  .blossom-sprig {
    position: absolute;
    top: 229px;
    width: 52px;
    height: 110px;
    background: var(--gold);
    border-radius: 26px 26px 12px 12px;
  }
  .blossom-sprig--left { left: 6px; }
  .blossom-sprig--right { left: 459px; }
  .tree-emblem {
    position: absolute;
    left: 188px;
    top: 109px;
    width: 144px;
    height: 86px;
    background: var(--gold);
    border-radius: 72px 72px 20px 20px;
  }
  .brand-name,
  .brand-sub,
  .scent-title,
  .product-facts {
    position: absolute;
    left: 0;
    width: 100%;
    text-align: center;
    color: var(--gold);
  }
  .brand-name {
    top: 205px;
    font-family: "Cormorant Garamond", serif;
    font-weight: 600;
    font-size: 38px;
    line-height: 1;
    letter-spacing: 5px;
    padding-left: 5px;
  }
  .brand-sub {
    top: 243px;
    font-family: "Alegreya Sans", sans-serif;
    font-weight: 400;
    font-size: 14px;
    line-height: 1;
    letter-spacing: 2.5px;
    padding-left: 2.5px;
  }
  .scent-title {
    top: 304px;
    font-family: "Great Vibes", cursive;
    font-weight: 400;
    font-size: 38px;
    line-height: 40px;
  }
  .product-facts {
    top: 427px;
    font-family: "Alegreya Sans", sans-serif;
    font-size: 15px;
    line-height: 19px;
  }
</style>
</head>
<body>
  <main class="canvas">
    <section class="sticker">
      <div class="frame"></div>
      <div class="blossom-sprig blossom-sprig--left" role="img" aria-label="Small flowering sprig ornament on the left edge of the frame"></div>
      <div class="blossom-sprig blossom-sprig--right" role="img" aria-label="Small flowering sprig ornament on the right edge of the frame"></div>
      <div class="tree-emblem" role="img" aria-label="Etched tree illustration in gold"></div>
      <p class="brand-name">ASHBROOK</p>
      <p class="brand-sub">CANDLE CO.</p>
      <h1 class="scent-title">Japanese Cherry<br>Blossom</h1>
      <p class="product-facts">Made in Australia<br>100% SOY WAX</p>
    </section>
  </main>
</body>
</html>
```